DL size flyer design for renovations and extensions construction company

We are looking for a flyer design for a construction company specialising in renovations, extensions, and minor building works. The aim is for anyone needing any home construction works to pick up the phone and call us. The flyers will be delivered primarily to letterboxes of homes. We want the flyers to stick out from all the other things people get in the mail by any means possible.

Target Market(s)

The audience we target is residential home owners and are looking to deliver these letters to home letterboxes.

Industry/Entity Type

Residential Construction

Font styles to use
Sans Serif

Colors
000000
ffffff

Requirements
Must have
• 1 - Places for 4 photos with descriptions reading: (1) Bathroom Renovations (4) Kitchen Renovations (3) Home Extensions (4) Outdoor works and landscaping. This may be on the reverse side of the DL flyer.
• 2 - Fonts to be used are (1) Brandon Grotesque (All caps) for main heading, (2) Montserrat SemiBold (All caps) for Headings, (3) Lato for text.
• 3 - Copy of the finished document in PDF and indesign formats.
• 4 - Placeholders for copy (look at the pelvaridge.com website for now)
Nice to have
• A modern looking design.
Should not have
• Not all photos attached are necessarily required. Up to you to use your creativity to decide on the best combination.

```html
<!DOCTYPE html>
<html lang="en">
<head>
<meta charset="utf-8">
<title>Pelvaridge Homes DL Flyer</title>
<link rel="stylesheet" href="https://fonts.googleapis.com/css2?family=Montserrat:wght@600;700;800&family=Lato:wght@400;700;900&display=swap">
<style>
:root{
  --green:#0a9a4c;
  --green-deep:#078a43;
  --green-dark:#06753a;
  --charcoal:#2f3033;
  --slate:#55575a;
  --ink:#111;
  --white:#fff;
  --band:#f1f2f2;
  --stage:#9c9c9c;
}
*{margin:0;padding:0;box-sizing:border-box}
html,body{width:1200px;height:943px;overflow:hidden}
body{background:var(--stage);position:relative;font-family:"Lato",sans-serif;color:var(--ink)}
.flyer{position:absolute;top:36px;width:511px;height:1021px;background:var(--white);transform:scale(.857);transform-origin:0 0;overflow:hidden}
.flyer--front{left:114px}
.flyer--back{left:620px}
.brand{position:absolute;left:0;right:0;text-align:center;font-family:"Montserrat",sans-serif;font-weight:800;color:var(--ink);letter-spacing:1px;white-space:nowrap}
.flyer--front .brand{top:66px;font-size:36px}
.flyer--back .brand{top:30px;font-size:28px}
.brand-dot{display:inline-block;width:14px;height:14px;background:var(--green);margin-right:10px;vertical-align:middle;position:relative;top:-3px}
.hero-photo{position:absolute;left:0;top:165px;width:511px;height:460px;background:linear-gradient(160deg,#f4f4f2 0%,#dfe3dc 35%,#c9bfb2 65%,#a89a89 100%)}
.shapes{position:absolute;left:0;top:0;width:511px;height:1021px}
.headline{position:absolute;left:0;right:0;top:740px;text-align:center;font-family:"Montserrat",sans-serif;font-weight:700;font-size:30px;line-height:40px;letter-spacing:.3px;text-transform:uppercase}
.headline .accent{color:var(--green)}
.services{position:absolute;top:852px;left:0;right:0;display:flex;justify-content:space-around;padding:0 30px}
.service{width:120px;text-align:center}
.service-icon{width:56px;height:56px;border-radius:50%;background:var(--green);margin:0 auto;display:flex;align-items:center;justify-content:center}
.service-label{margin-top:22px;font-family:"Montserrat",sans-serif;font-weight:600;font-size:19px;letter-spacing:.5px}
.site{position:absolute;left:0;right:0;text-align:center;font-family:"Lato",sans-serif;font-size:19px;display:flex;align-items:center;justify-content:center;gap:10px}
.flyer--front .site{top:980px}
.flyer--back .site{top:982px}
.site b{color:var(--green);font-weight:900}
.site .rule{width:76px;height:3px;background:var(--green)}
.service-row{position:absolute;left:0;width:511px;height:145px}
.service-row--shade{background:linear-gradient(90deg,var(--band),#fafafa)}
.thumb{position:absolute;width:170px;height:112px;border:4px solid #d8d4cc;padding:5px}
.thumb::after{content:"";position:absolute;inset:5px;border:2px solid rgba(255,255,255,.9)}
.thumb--bath{background:linear-gradient(120deg,#f2f2f0,#c9c9c6 60%,#8e8e8a)}
.thumb--kitchen{background:linear-gradient(120deg,#e9e9e6,#c5c4be 55%,#a6a39b)}
.thumb--ext{background:linear-gradient(120deg,#f3f0ea,#c9936a 60%,#5f6e4a)}
.thumb--outdoor{background:linear-gradient(120deg,#eeeeec,#bcbcb8 55%,#7b7b77)}
.row-copy{position:absolute;width:250px}
.row-title{font-family:"Montserrat",sans-serif;font-weight:700;font-size:17px;color:var(--green);text-transform:uppercase;line-height:23px;margin-bottom:4px}
.row-text{font-size:14.5px;line-height:18px;color:#222}
.cta{position:absolute;left:0;right:0;top:830px;text-align:center}
.cta-lead{font-family:"Montserrat",sans-serif;font-weight:700;font-size:28px;display:inline-flex;align-items:center;gap:4px}
.cta-lead span{background:var(--green);color:var(--white);border-radius:6px;padding:0 6px;line-height:36px}
.cta-phone{font-family:"Montserrat",sans-serif;font-weight:700;font-size:42px;letter-spacing:.5px;margin-top:2px}
.contact{position:absolute;left:0;right:0;top:936px;display:flex;justify-content:center;align-items:center;gap:14px;font-size:15px}
.contact .divider{width:2px;height:28px;background:var(--green)}
.contact-item{display:flex;align-items:center;gap:8px}
</style>
</head>
<body>

<section class="flyer flyer--front">
  <div class="brand"><span class="brand-dot"></span>PELVARIDGE HOMES</div>
  <div class="hero-photo" role="img" aria-label="Family of four gathered around a bright white kitchen island"></div>
  <svg class="shapes" viewBox="0 0 511 1021" aria-hidden="true">
    <polygon points="0,548 300,595 511,548 511,666 0,640" fill="var(--green)"/>
    <polygon points="300,595 511,548 511,666" fill="var(--green-dark)"/>
    <polygon points="0,624 0,728 215,672" fill="var(--slate)"/>
    <polygon points="0,624 215,672 120,690" fill="var(--charcoal)"/>
    <polygon points="0,728 215,672 511,666 511,1021 0,1021" fill="var(--white)"/>
  </svg>
  <h1 class="headline">Looking to make your<br><span class="accent">home bigger or better?</span></h1>
  <div class="services">
    <div class="service">
      <div class="service-icon"><svg width="32" height="32" viewBox="0 0 32 32"><g stroke="#fff" stroke-width="4" stroke-linecap="round"><line x1="6" y1="26" x2="24" y2="8"/><line x1="8" y1="8" x2="26" y2="26"/></g><rect x="19" y="3" width="10" height="6" fill="#fff" transform="rotate(45 24 6)"/></svg></div>
      <div class="service-label">BUILD</div>
    </div>
    <div class="service">
      <div class="service-icon"><svg width="34" height="34" viewBox="0 0 34 34"><rect x="10" y="7" width="14" height="20" fill="#fff"/><g fill="var(--green)"><rect x="12" y="10" width="3" height="3"/><rect x="19" y="10" width="3" height="3"/><rect x="12" y="16" width="3" height="3"/><rect x="19" y="16" width="3" height="3"/></g><path d="M4 17a13 13 0 0 1 21-10M30 17a13 13 0 0 1-21 10" stroke="#fff" stroke-width="2.5" fill="none"/></svg></div>
      <div class="service-label">RENOVATE</div>
    </div>
    <div class="service">
      <div class="service-icon"><svg width="32" height="32" viewBox="0 0 32 32"><g stroke="#fff" stroke-width="3" fill="none" stroke-linecap="round"><path d="M5 12V5h7M5 5l8 8M27 12V5h-7M27 5l-8 8M5 20v7h7M5 27l8-8M27 20v7h-7M27 27l-8-8"/></g></svg></div>
      <div class="service-label">EXTEND</div>
    </div>
  </div>
  <div class="site"><span class="rule"></span>www.<b>pelvaridge</b>.com<span class="rule"></span></div>
</section>

<section class="flyer flyer--back">
  <div class="brand"><span class="brand-dot"></span>PELVARIDGE HOMES</div>

  <div class="service-row" style="top:80px">
    <div class="thumb thumb--bath" style="left:32px;top:15px" role="img" aria-label="Modern bathroom with freestanding bath and glass shower"></div>
    <div class="row-copy" style="left:228px;top:30px">
      <h2 class="row-title">Bathroom Renovations</h2>
      <p class="row-text">We create custom bathroom renovations of various shapes and sizes to suit a variety of family needs.</p>
    </div>
  </div>

  <div class="service-row service-row--shade" style="top:223px">
    <div class="thumb thumb--kitchen" style="left:312px;top:17px" role="img" aria-label="Contemporary kitchen with grey cabinetry"></div>
    <div class="row-copy" style="left:30px;top:30px">
      <h2 class="row-title">Kitchen Renovations</h2>
      <p class="row-text">Today's kitchens go further than places to just make a meal - they are the open-plan hub for the modern home.</p>
    </div>
  </div>

  <div class="service-row" style="top:368px">
    <div class="thumb thumb--ext" style="left:32px;top:20px" role="img" aria-label="Open-plan dining extension with timber floor"></div>
    <div class="row-copy" style="left:228px;top:16px">
      <h2 class="row-title">Home Extensions</h2>
      <p class="row-text">Pelvaridge Homes are licenced builders experienced at delivering structural alterations or home extensions, and we are always guided by our qualified engineers.</p>
    </div>
  </div>

  <div class="service-row service-row--shade" style="top:518px">
    <div class="thumb thumb--outdoor" style="left:312px;top:17px" role="img" aria-label="Light-filled bathroom opening to garden view"></div>
    <div class="row-copy" style="left:30px;top:14px">
      <h2 class="row-title">Outdoor works and<br>landscaping</h2>
      <p class="row-text">Home living spans across both internal and external environments and a complete home needs to consider integration into the surrounding land.</p>
    </div>
  </div>

  <svg class="shapes" viewBox="0 0 511 1021" aria-hidden="true">
    <polygon points="0,676 250,730 511,676 511,796 0,756" fill="var(--green)"/>
    <polygon points="250,730 511,676 511,796" fill="var(--green-deep)"/>
    <polygon points="0,754 0,858 200,780" fill="var(--slate)"/>
    <polygon points="0,754 200,780 100,810" fill="var(--charcoal)"/>
    <polygon points="0,858 200,780 511,796 511,1021 0,1021" fill="var(--white)"/>
  </svg>

  <div class="cta">
    <div class="cta-lead">REQUEST <span>A QUOTE</span></div>
    <div class="cta-phone">0412 555 019</div>
  </div>
  <div class="contact">
    <div class="contact-item"><svg width="14" height="10" viewBox="0 0 14 10"><rect width="14" height="10" fill="var(--green)"/><path d="M0 0l7 6 7-6" stroke="#fff" stroke-width="1.3" fill="none"/></svg>info@pelvaridge.com</div>
    <span class="divider"></span>
    <div class="contact-item"><svg width="11" height="15" viewBox="0 0 11 15"><path d="M5.5 0A5.5 5.5 0 0 0 0 5.5C0 9.5 5.5 15 5.5 15S11 9.5 11 5.5A5.5 5.5 0 0 0 5.5 0z" fill="var(--green)"/><circle cx="5.5" cy="5.5" r="2" fill="#fff"/></svg>Sydney, NSW.</div>
  </div>
  <div class="site"><span class="rule"></span>www.<b>pelvaridge</b>.com<span class="rule"></span></div>
</section>

</body>
</html>
```